Financial Advisor needs a BOLD Business Card

I need a business card that is professional, and is also eye-catching and memorable. I would like to include my photo (several different professional photos have been uploaded). Preferred primary color is blue, or green, or dark purple. The final design should have a modern/contemporary look while communicating a professional image.

Target Market(s)

Individual Investors and Small Business Owners

Industry/Entity Type

Business

Contact Information for Business Card

[side 1:] Dale Varkonen Financial Advisor 58217 Marlow Brook Rd., #240 St. Louis, MO 63975 (314) 555-0187 main (314) 555-0142 cell (314) 555-0169 fax dalev@qrmvbk.com [side 2:] Life Insurance | Retirement | Employee Benefits

Font styles to use
Serif
Sans Serif

Requirements
Must have
• [disclaimer, text can be 7-9 point:] Securities offered through the K.R. Capital Trading Company. Member BLUDA/TAVK. Nine Harbor Circle, Cincinnati, Ohio 45817. 513-555-0123. Investment Advisory Services offered through K.R. Portfolio Stewardship Company.
Nice to have
• Bright, Light & Airy feel on Side 1 with contact data, bold patterns, high color contrast, modern or 3D look
Should not have
• Any symbols referring to money (e.g. $)

```html
<!DOCTYPE html>
<html lang="en">
<head>
<meta charset="utf-8">
<title>Dale Varkonen – Business Card</title>
<link rel="stylesheet" href="https://fonts.googleapis.com/css2?family=Poppins:ital,wght@0,300;0,400;0,600;1,400&display=swap">
<style>
  :root {
    --teal: #1ab4cf;
    --teal-dark: #1597b0;
    --ink: #2b2b2b;
    --grey: #6f6f6f;
    --purple: #5a2a6e;
    --paper: #ffffff;
    --backdrop: #e9ecee;
  }
  * { box-sizing: border-box; margin: 0; padding: 0; }
  html, body { width: 1200px; height: 873px; overflow: hidden; }
  body {
    background: var(--backdrop);
    font-family: "Poppins", sans-serif;
    position: relative;
  }
  .card {
    position: absolute;
    left: 260px;
    width: 680px;
    height: 389px;
    border-radius: 4px;
    box-shadow: 0 6px 18px rgba(0,0,0,.12);
    overflow: hidden;
  }
  .card--front { top: 32px; background: var(--paper); }
  .card--back { top: 452px; background: var(--teal); }

  .portrait {
    position: absolute;
    left: 112px; top: 34px;
    width: 92px; height: 92px;
    border-radius: 50%;
    border: 3px solid var(--teal);
    background: radial-gradient(circle at 50% 40%, #b9b2ab 0%, #6d6a6a 55%, #3f4a58 100%);
  }
  .identity { position: absolute; left: 52px; top: 132px; }
  .identity__name { font-size: 25px; color: var(--ink); line-height: 1.1; letter-spacing: -.2px; }
  .identity__first { font-weight: 300; }
  .identity__last { font-weight: 600; }
  .identity__title { font-size: 16px; font-style: italic; color: var(--teal); margin-top: 2px; }

  .contact {
    position: absolute;
    right: 40px; top: 150px;
    list-style: none;
    text-align: right;
    font-size: 16px;
    color: var(--ink);
    line-height: 1.35;
  }
  .contact li { display: flex; justify-content: flex-end; align-items: flex-start; gap: 8px; }
  .contact svg { width: 13px; height: 13px; margin-top: 4px; flex: none; }
  .contact__icon { fill: none; stroke: var(--teal); stroke-width: 2; }
  .contact__icon--pin { stroke: var(--purple); }

  .disclaimer {
    position: absolute;
    left: 52px; bottom: 34px;
    width: 560px;
    font-size: 11.5px;
    line-height: 1.35;
    color: var(--grey);
  }

  .services {
    position: absolute;
    left: 44px; top: 40px;
    font-size: 19px;
    font-weight: 600;
    color: var(--paper);
    letter-spacing: .6px;
  }
</style>
</head>
<body>

<section class="card card--front">
  <div class="portrait" role="img" aria-label="Portrait photo of Dale Varkonen"></div>
  <div class="identity">
    <p class="identity__name"><span class="identity__first">Dale</span><span class="identity__last">Varkonen</span></p>
    <p class="identity__title">Financial Advisor</p>
  </div>

  <ul class="contact">
    <li>(314) 555-0187
      <svg viewBox="0 0 14 14" class="contact__icon"><path d="M3 1.5 5 4 3.8 5.5c.8 1.8 2.3 3.3 4.7 4.7L10 9l2.5 2-1.2 1.8C6 12.5 1.5 8 1.2 2.7Z"/></svg></li>
    <li>(314) 555-0142
      <svg viewBox="0 0 14 14" class="contact__icon"><rect x="3.5" y="1" width="7" height="12" rx="1.2"/><path d="M6 11h2"/></svg></li>
    <li>(314) 555-0169
      <svg viewBox="0 0 14 14" class="contact__icon"><rect x="1.5" y="5" width="11" height="7" rx="1"/><path d="M4 5V1.5h6V5M4 8.5h6"/></svg></li>
    <li>dalev@qrmvbk.com
      <svg viewBox="0 0 14 14" class="contact__icon"><rect x="1" y="3" width="12" height="8.5" rx="1"/><path d="m1.5 3.5 5.5 4.5 5.5-4.5"/></svg></li>
    <li>58217 Marlow Brook Rd., #240 St.<br>Louis, MO 63975
      <svg viewBox="0 0 14 14" class="contact__icon contact__icon--pin"><path d="M7 13s4.5-4.5 4.5-7.5a4.5 4.5 0 0 0-9 0C2.5 8.5 7 13 7 13Z"/><circle cx="7" cy="5.5" r="1.5"/></svg></li>
  </ul>

  <p class="disclaimer">Securities offered through the K.R. Capital Trading Company. Member BLUDA/TAVK. Nine Harbor Circle, Cincinnati, Ohio 45817. 513-555-0123. Investment Advisory Services offered through K.R. Portfolio Stewardship Company.</p>
</section>

<section class="card card--back">
  <p class="services">Life Insurance | Retirement | Employee Benefits</p>
</section>

</body>
</html>
```